Travinex - You are the Boss!

Travinex is a new Silicon Valley company, of the pelim founders from Berlin, which provides a "Shared Pioneer Circle". This platform allows the crowd to support startups with money, experts and fame. Our Vision is, that everyone should become an entrepreneur.

Pls find all brief details in the attached document
Updates

Would be nice to have a list of more social services I'm available on, like a list of pictograms of all my services:

Find me on: vooka, bramlet+, qrt, fenwix, moodrail, zupp, hvoxa, etc...

pls make sure to use the right font:
http://www.typemarlow.com/fonts/Velquin

Target Market(s)

Main target market is those already involved in the startup industry, by fundraising, investing, advising, cofounding and working. Travinex brings a totaly new transparency and collaborative way of starting companies to that business.

· Entrepreneurs (looking for funding, team and community)
· Investors (looking for hot investments and )
· Experts (workers looking for startups they can work for equity)
· Incubators & Business Schools (looking for tools to advise startups)

Industry/Entity Type

It Company

Requirements
Must have
• Pls find all brief details in the attached document
Nice to have

```html
<!DOCTYPE html>
<html lang="en">
<head>
<meta charset="utf-8">
<title>Travinex – Business Card</title>
<link rel="stylesheet" href="https://fonts.googleapis.com/css2?family=Exo+2:wght@400;600&display=swap">
<style>
  :root {
    --stage: #000000;
    --orange-deep: #ef5a24;
    --orange-mid: #f47a2a;
    --orange-light: #f7962e;
    --paper: #ffffff;
    --ink: #1c1c1c;
    --name-grey: #3a3a3a;
    --muted: #8a8a8a;
  }
  html, body {
    margin: 0;
    width: 1200px;
    height: 1173px;
    overflow: hidden;
    background: var(--stage);
  }
  .canvas {
    position: relative;
    width: 1200px;
    height: 1173px;
  }
  .card {
    position: absolute;
    left: 260px;
    width: 688px;
    border-radius: 32px;
    overflow: hidden;
    background: var(--paper);
  }
  .brand-name {
    position: absolute;
    margin: 0;
    font-family: "Exo 2", sans-serif;
    font-weight: 600;
    font-size: 56px;
    line-height: 1;
    letter-spacing: 2px;
    color: var(--name-grey);
    white-space: nowrap;
  }

  /* ---------- Front ---------- */
  .card--front { top: 163px; height: 398px; }
  .front__top {
    position: absolute; left: 0; top: 0; width: 100%; height: 108px;
    background: radial-gradient(ellipse at 60% 40%, var(--orange-light), var(--orange-deep) 80%);
  }
  .front__band {
    position: absolute; left: 0; top: 108px; width: 100%; height: 141px;
    background: var(--paper);
  }
  .front__bottom {
    position: absolute; left: 0; top: 249px; width: 100%; height: 149px;
    background: linear-gradient(180deg, var(--orange-mid), var(--orange-deep));
  }
  .brand-dot {
    position: absolute; left: 160px; top: 143px;
    width: 70px; height: 70px; border-radius: 50%;
    background: var(--orange-deep);
  }
  .card--front .brand-name { left: 255px; top: 150px; }
  .front__invite {
    position: absolute; left: 0; right: 0; top: 325px;
    margin: 0;
    text-align: center;
    font-family: "Exo 2", sans-serif;
    font-size: 18px;
    line-height: 27px;
    color: var(--paper);
  }

  /* ---------- Back ---------- */
  .card--back { top: 615px; height: 393px; }
  .card--back .brand-name { left: 138px; top: 80px; }
  .back__band-left {
    position: absolute; left: 0; top: 167px; width: 322px; height: 58px;
    background: linear-gradient(90deg, var(--orange-deep), var(--orange-mid));
  }
  .back__band-right {
    position: absolute; left: 566px; top: 167px; width: 122px; height: 58px;
    background: linear-gradient(90deg, var(--orange-mid), var(--orange-light));
  }
  .holder {
    position: absolute; left: 338px; top: 177px;
    font-family: "Exo 2", sans-serif;
    color: var(--ink);
  }
  .holder__name { margin: 0; font-size: 20px; font-weight: 600; line-height: 22px; }
  .holder__role { margin: 2px 0 0; font-size: 12px; line-height: 14px; }
  .contacts {
    position: absolute; left: 22px; top: 250px;
    margin: 0; padding: 0; list-style: none;
    font-family: "Exo 2", sans-serif;
    font-size: 14px;
    color: var(--muted);
  }
  .contacts li { height: 24px; line-height: 24px; }
  .contacts__label { display: inline-block; width: 38px; }
</style>
</head>
<body>
<main class="canvas">

  <section class="card card--front" aria-label="Card front">
    <div class="front__top"></div>
    <div class="front__band"></div>
    <div class="front__bottom"></div>
    <span class="brand-dot" aria-hidden="true"></span>
    <h1 class="brand-name">TRAVINEX</h1>
    <p class="front__invite">Are you interested in Startups, Investments, Work?<br>Join: friendwall.net/Travinex</p>
  </section>

  <section class="card card--back" aria-label="Card back">
    <h2 class="brand-name">TRAVINEX</h2>
    <div class="back__band-left"></div>
    <div class="back__band-right"></div>
    <div class="holder">
      <p class="holder__name">Jonas Weller</p>
      <p class="holder__role">Founder and CEO</p>
    </div>
    <ul class="contacts">
      <li><span class="contacts__label">P:</span>+44 - 201 - 555 - 0147</li>
      <li><span class="contacts__label">E:</span>the@travinex.com</li>
      <li><span class="contacts__label">T:</span>chirpline.net/jonasweller</li>
      <li><span class="contacts__label">F:</span>friendwall.net/jonasweller</li>
      <li><span class="contacts__label">L:</span>linkwork.net/in/jonasweller</li>
    </ul>
  </section>

</main>
</body>
</html>
```